依頼概要
▽ターゲット
【■ 40~80歳■】向けの【■ ふとんの打ち直し■】販促用にポスターデザインを作成したいと考えており、デザイナー・クリエイターの方向けにコンペを開催いたします。

▽サイズ
【■A2サイズでトンボを付けて下さい。そのまま印刷屋に出せる形式(AIファイル必須■】

▽参考デザイン
サイト名:【■ ねむり堂川 ■】
参考URL:【■ http://www.nemuridokawa.co.jp/SHOP/582716/list.html■】

```html
<!DOCTYPE html>
<html lang="ja">
<head>
<meta charset="utf-8">
<title>ふとん 仕立て直し承ります</title>
<link href="https://fonts.googleapis.com/css2?family=M+PLUS+Rounded+1c:wght@500;800;900&family=Zen+Maru+Gothic:wght@500;700&display=swap" rel="stylesheet">
<style>
:root{
  --sky:#5ec6ee;
  --paper:#ffffff;
  --red:#e60012;
  --orange:#f39800;
  --ink:#222222;
  --futon-pink:#f7b7cf;
  --futon-deep:#e98fb3;
}
*{margin:0;padding:0;box-sizing:border-box}
html,body{width:867px;height:1200px;overflow:hidden;background:var(--sky)}
body{font-family:"Zen Maru Gothic","M PLUS Rounded 1c",sans-serif;color:var(--ink)}
.poster{position:relative;width:867px;height:1200px;background:var(--sky)}
.sheet{position:absolute;left:34px;top:40px;width:799px;height:1010px;background:var(--paper);border-radius:60px}
.title-block{position:absolute;left:70px;top:62px;width:190px;height:550px;background:var(--red);border-radius:28px;
  display:flex;flex-direction:column;align-items:center;justify-content:space-around;padding:10px 0}
.title-block span{font-family:"M PLUS Rounded 1c",sans-serif;font-weight:900;font-size:150px;line-height:1;color:var(--paper)}
.service{position:absolute;left:76px;top:622px;font-family:"M PLUS Rounded 1c",sans-serif;font-weight:800;font-size:36px;line-height:1.2;color:var(--ink);white-space:nowrap}
.service .indent{display:block;padding-left:44px}
.lead{position:absolute;left:300px;top:72px;font-family:"M PLUS Rounded 1c",sans-serif;font-weight:800;font-size:26px;line-height:1.42;color:var(--orange);white-space:nowrap}
.sleeper{position:absolute;left:420px;top:200px;width:340px;height:290px;border-radius:40px 40px 60px 60px;
  background:linear-gradient(180deg,#fbe3ec 0%,var(--futon-pink) 55%,var(--futon-deep) 100%)}
.prices{position:absolute;left:405px;top:500px;font-family:"M PLUS Rounded 1c",sans-serif;font-weight:900;color:var(--red);font-size:36px;line-height:1.45;white-space:nowrap}
.prices li{list-style:none;display:flex}
.prices .size{width:210px}
.section-head{position:absolute;left:76px;font-family:"M PLUS Rounded 1c",sans-serif;font-weight:800;font-size:30px;color:var(--orange);
  border-bottom:3px solid var(--orange);padding-bottom:2px;white-space:nowrap}
.head-new{top:722px}
.head-common{top:878px}
.note{position:absolute;left:76px;font-size:17px;line-height:1.5;font-weight:500;white-space:nowrap}
.note-new{top:774px}
.note-common{top:930px}
.campaign{position:absolute;left:600px;top:680px;font-family:"M PLUS Rounded 1c",sans-serif;font-weight:900;font-size:30px;color:var(--orange);
  transform:rotate(28deg);transform-origin:left top;white-space:nowrap}
.shop{position:absolute;left:80px;top:1075px;width:707px;height:90px;background:var(--paper);border-radius:40px;display:flex;align-items:center;padding-left:30px}
.shop .tag{font-size:22px;font-weight:700;white-space:nowrap}
.shop .name{font-family:"M PLUS Rounded 1c",sans-serif;font-weight:900;font-size:40px;margin-left:12px;white-space:nowrap}
.shop .ask{position:absolute;right:30px;bottom:14px;font-size:15px;white-space:nowrap}
</style>
</head>
<body>
<main class="poster">
  <div class="sheet"></div>
  <h1 class="title-block"><span>ふ</span><span>と</span><span>ん</span></h1>
  <p class="service">仕立て直し<span class="indent">承ります</span></p>
  <p class="lead">お布団を干してもふんわりしない<br>敷布団は３年・掛け布団で５年が目安<br>そんな時は、新品・打ち直し！！</p>
  <div class="sleeper" role="img" aria-label="ピンクの布団で眠る人のイラスト"></div>
  <ul class="prices">
    <li><span class="size">シングル</span><span>¥8,800～</span></li>
    <li><span class="size">セミダブル</span><span>¥9,800～</span></li>
    <li><span class="size">ダブル</span><span>¥10,800～</span></li>
  </ul>
  <h2 class="section-head head-new">新品の詳細について</h2>
  <p class="campaign">キャンペーン実施中</p>
  <p class="note note-new">掛けの中綿は少し割高ですが、新品がおすすめです！<br>新品の布団は上記各サイズより3,000円程足した料金でお求め頂けます。<br>（素材は保温性・吸湿性の高い綿を使用しています）</p>
  <h2 class="section-head head-common">仕立て直し、新品共通の詳細について</h2>
  <p class="note note-common">側は「おまかせ」で別料金・生地から選んで頂けます。<br>ロング丈（10cm長）は¥1,000加算でございます。<br>尚、枕やカバー等もご用意出来ます。</p>
  <footer class="shop">
    <span class="tag">クリーニングと寝具の店</span>
    <span class="name">ふとんの北浜</span>
    <span class="ask">詳しくは店主まで</span>
  </footer>
</main>
</body>
</html>
```